Electronic Cigarette company needs Signage Design

We are Vapowen electronic cigarette company. We are looking to have signage created to place on store front doors and windows, as well as inside on counters for customers to see.

Some of the benefits of electronic cigarettes are:
-No Carcinogens
-No Tar
-Odorless

Our electronic cigarette are equal to over 2 packs of traditional tobacco cigarettes. The savings on these are just as good as the health benefits to it.

These signs should be similar to a zestmoo or other ads you would see to attract customers.

We can assure you that the designer we choose for this, will have much more projects in the near future for numerous other business logos and advertising designs. This is our first project being done on this site and we are hoping to see the same quality design like we have throughout the site.

If more than one are quality banners, we will consider a price second or third place offer.

Please let me know any information you may need to help with the design work.
Updates

Reason: The reason for the extension is due to the fact that i have not received a quality product yet. This is to be displayed on store fronts as an ad. Most design post have not been an add just putting some color on the logo. Please just use existing logo, address the Cost and savings factor. Use your marketing skills for this please.

Reason: Still have not received a design meeting the requirements. Please message me any questions to help guide this project down the right path.

I have posted pictures of our product that i have received, we have yet to get a design that we are happy with so please, any questions about a path to go please message me. 

Industry/Entity Type

Advertising

Requirements
Nice to have
• We would like to see something with a photo of our product, maybe sticking out of the side for an odd cut ad. The problem is our packaging isn't completed yet but i do have design photos that i am sure you guys could utilize.

```html
<!DOCTYPE html>
<html lang="en">
<head>
<meta charset="utf-8">
<title>Vapowen Electronic Cigarette Sign</title>
<link href="https://fonts.googleapis.com/css2?family=Arimo:wght@400;700&display=swap" rel="stylesheet">
<style>
  :root {
    --bg-light: #f4f4f4;
    --bg-mid: #e3e3e3;
    --bg-deep: #d2d2d2;
    --brand-blue: #3a62a8;
    --pack-green: #1f9a3a;
    --pack-blue: #3d6fb5;
    --tick-green: #2da034;
    --pack-white: #ffffff;
    --small-grey: #5a6f8f;
  }
  * { margin: 0; padding: 0; box-sizing: border-box; }
  html, body {
    width: 1200px; height: 814px; overflow: hidden;
    background: var(--bg-mid);
    font-family: "Arimo", Arial, sans-serif;
  }
  .sign {
    position: relative; width: 1200px; height: 814px;
    background: linear-gradient(180deg, var(--bg-light) 0%, var(--bg-mid) 70%, var(--bg-light) 100%);
    overflow: hidden;
  }
  .hero-photo {
    position: absolute; left: 480px; top: 0; width: 720px; height: 814px;
    background: radial-gradient(ellipse at 65% 55%, #e9d2bf 0%, #dcc7b6 22%, var(--bg-mid) 52%, transparent 75%);
  }
  .pack {
    position: absolute; top: 56px;
    background: var(--pack-white);
    box-shadow: 4px 6px 10px rgba(0,0,0,0.18);
    display: flex; flex-direction: column; align-items: center;
  }
  .pack--green { left: 40px; width: 122px; height: 694px; --pack: var(--pack-green); }
  .pack--blue { left: 166px; width: 112px; height: 672px; --pack: var(--pack-blue); }
  .pack__cap {
    width: 100%; height: 88px; background: var(--pack);
    color: var(--pack-white); font-weight: 700; font-size: 15px; line-height: 1.2;
    text-align: center; display: flex; align-items: center; justify-content: center;
  }
  .pack__label {
    flex: 1; display: flex; flex-direction: row-reverse; align-items: flex-start;
    justify-content: center; gap: 4px; padding-top: 30px;
  }
  .pack__brand, .pack__claims { writing-mode: vertical-rl; }
  .pack__brand {
    font-weight: 700; font-size: 50px; color: var(--brand-blue); letter-spacing: 1px;
  }
  .pack__mark {
    display: block; width: 34px; height: 34px; border-radius: 50%;
    background: var(--brand-blue); margin-bottom: 14px;
  }
  .pack__brand-wrap { display: flex; flex-direction: column; align-items: center; }
  .pack__claims { font-size: 13px; color: var(--small-grey); padding-top: 56px; }
  .pack__foot {
    width: 100%; height: 104px; background: var(--pack);
    color: var(--pack-white); font-weight: 700; font-size: 18px; line-height: 1.25;
    text-align: center; display: flex; align-items: center; justify-content: center;
  }
  .benefits {
    position: absolute; left: 300px; top: 86px; list-style: none;
  }
  .benefits__item {
    display: flex; align-items: center; gap: 10px; height: 84px;
    font-weight: 700; font-size: 46px; color: var(--brand-blue);
  }
  .benefits__tick { width: 46px; height: 46px; flex: none; }
</style>
</head>
<body>
<main class="sign">
  <div class="hero-photo" role="img" aria-label="Photo of a fist crushing a pack of tobacco cigarettes on a white table"></div>

  <div class="pack pack--green">
    <div class="pack__cap">Equal To<br>Over<br>2 Packs</div>
    <div class="pack__label">
      <div class="pack__brand-wrap"><span class="pack__mark"></span><span class="pack__brand">Vapowen</span></div>
      <span class="pack__claims">No Tar No Carcinogens Odorless</span>
    </div>
    <div class="pack__foot">Electronic<br>Cigarette</div>
  </div>

  <div class="pack pack--blue">
    <div class="pack__cap">Equal To<br>Over<br>2 Packs</div>
    <div class="pack__label">
      <div class="pack__brand-wrap"><span class="pack__mark"></span><span class="pack__brand">Vapowen</span></div>
      <span class="pack__claims">No Tar No Carcinogens Odorless</span>
    </div>
    <div class="pack__foot">Electronic<br>Cigarette</div>
  </div>

  <ul class="benefits">
    <li class="benefits__item">
      <svg class="benefits__tick" viewBox="0 0 46 46" aria-hidden="true"><path d="M5 25 L17 38 L41 6" fill="none" stroke="var(--tick-green)" stroke-width="6" stroke-linecap="round" stroke-linejoin="round"/></svg>
      No Tar
    </li>
    <li class="benefits__item">
      <svg class="benefits__tick" viewBox="0 0 46 46" aria-hidden="true"><path d="M5 25 L17 38 L41 6" fill="none" stroke="var(--tick-green)" stroke-width="6" stroke-linecap="round" stroke-linejoin="round"/></svg>
      No Carcinogens
    </li>
    <li class="benefits__item">
      <svg class="benefits__tick" viewBox="0 0 46 46" aria-hidden="true"><path d="M5 25 L17 38 L41 6" fill="none" stroke="var(--tick-green)" stroke-width="6" stroke-linecap="round" stroke-linejoin="round"/></svg>
      Odorless
    </li>
  </ul>
</main>
</body>
</html>
```